Brisk Hive 360 Postcard Design, Double-Sided

Please read carefully and see attached. Designers that do not follow these instructions will not be selected. Limit ONE design submission per artist. The ONE design submission shall show both the front and the back designs. Designs must comply with the attached dismensions accounting for the bleed area to prevent designs from being cut off during printing. The attached business card and door tag designs have already been created, printed and are in use. The postcard shall be similar in design to the attached business card and door tag. All of the information that you need is attached. The overall size is 4.12" x 6.12" for the front. The back is different, see attached and scale to match template. I would like the Veteran Owned Business logo added as well. It would also be nice to see my photo incorporated somehow. I like the yellow on the door tag. It helps build contrast and pops out. Again, one design submission per designer that shows both the front and the back.

Target Market(s)

Please read all instructions and see attached.

Industry/Entity Type

Requirements
Must have
• Please read all instructions and see attached.
Nice to have
Should not have

```html
<!DOCTYPE html>
<html lang="en">
<head>
<meta charset="utf-8">
<title>Brisk Hive 360 Postcard – Front and Back</title>
<link rel="stylesheet" href="https://fonts.googleapis.com/css2?family=Anton&family=Roboto+Condensed:wght@300;400;700&display=swap">
<style>
  :root{
    --ink:#0b0b0b;
    --yellow:#f4ea12;
    --red:#e3232b;
    --panel:#e2e3e7;
    --paper:#ffffff;
    --stage:#f2f2f2;
  }
  *{box-sizing:border-box;margin:0;padding:0}
  html,body{width:1195px;height:1200px;overflow:hidden;background:var(--stage)}
  body{position:relative;font-family:"Roboto Condensed",sans-serif;color:var(--ink)}
  .card{position:absolute;top:411px;width:560px;height:377px;background:var(--paper);overflow:hidden;box-shadow:0 4px 12px rgba(0,0,0,.25)}
  .card--front{left:25px;background:var(--ink)}
  .card--back{left:610px}
  .shape{position:absolute;left:0;top:0}
  .brand-title{position:absolute;font-family:"Anton",sans-serif;color:var(--yellow);font-size:34px;line-height:1;letter-spacing:.5px;text-align:center;width:228px}
  .brand-rule{position:absolute;height:2px;background:var(--yellow)}
  .brand-sub{position:absolute;font-family:"Roboto Condensed",sans-serif;font-weight:400;color:var(--yellow);font-size:27px;line-height:1;text-align:center;width:228px;letter-spacing:.5px}
  .mark{position:absolute;display:flex;align-items:center;gap:6px;color:#fff;font-weight:700;font-size:13px;white-space:nowrap}
  .mark__dot{width:16px;height:16px;border-radius:50%;background:#fff}
  .badge{position:absolute;border-radius:50%;background:linear-gradient(#1d3b8b 0 55%,#d8202a 55%);border:3px solid #fff}
  .photo{position:absolute}
  .owner-panel{position:absolute;left:318px;top:129px;width:216px;height:191px}
  .owner-name{position:absolute;left:0;top:52px;width:216px;text-align:center;font-weight:700;font-size:24px;line-height:1}
  .owner-role{position:absolute;left:0;top:78px;width:216px;text-align:center;font-weight:400;font-size:15px;letter-spacing:.3px}
  .perks{position:absolute;left:64px;top:110px;list-style:none;font-size:14px;line-height:18px}
  .perks li::before,.services li::before{content:"• "}
  .services-title{position:absolute;left:18px;top:237px;font-family:"Anton",sans-serif;color:var(--red);font-size:21px}
  .services{position:absolute;list-style:none;font-size:14px;line-height:18px}
  .contact-bar{position:absolute;left:0;top:333px;width:560px;height:44px;background:var(--ink);border-top-right-radius:14px;display:flex;align-items:center;justify-content:space-between;padding:0 18px;color:#fff;font-size:12px}
  .contact{display:flex;align-items:center;gap:6px;white-space:nowrap}
  .contact svg{flex:none}
  .text-flag{color:var(--red)}
  .back-block{position:absolute;left:0;top:0;width:285px;height:299px;background:var(--ink)}
  .back-contacts{position:absolute;left:0;top:299px;width:138px;height:78px;background:var(--panel);padding:6px 0 0 8px;list-style:none;font-size:9.5px;line-height:15px}
  .back-contacts .contact{gap:4px}
  .stamp-box{position:absolute;left:446px;top:17px;width:97px;height:96px;border:1.5px solid var(--ink)}
</style>
</head>
<body>

<section class="card card--front" aria-label="Postcard front">
  <svg class="shape" width="560" height="377" viewBox="0 0 560 377" aria-hidden="true">
    <polygon points="0,176 141,226 318,170 318,180 141,240 0,186" fill="var(--yellow)"/>
    <polygon points="0,186 141,240 318,180 318,160 560,129 560,377 0,377" fill="var(--paper)"/>
    <path d="M318 156 L528 129 Q534 128 534 136 L534 310 Q534 320 524 320 L328 320 Q318 320 318 310 Z" fill="var(--panel)"/>
  </svg>

  <div class="brand-title" style="left:26px;top:17px">BRISK HIVE 360</div>
  <div class="brand-rule" style="left:28px;top:55px;width:224px"></div>
  <div class="brand-sub" style="left:26px;top:59px">HANDYMAN</div>

  <div class="mark" style="left:90px;top:138px"><span class="mark__dot"></span>BRISK HIVE 360</div>

  <div class="photo" role="img" aria-label="Portrait photo of the owner in a grey uniform shirt" style="left:340px;top:12px;width:140px;height:150px;background:linear-gradient(180deg,#3a3a3a,#8d8f94 60%,#b9bbc0)"></div>
  <div class="badge" role="img" aria-label="Veteran owned business badge" style="left:468px;top:14px;width:72px;height:72px"></div>

  <div class="owner-panel">
    <div class="owner-name">DALTON R.MEYER</div>
    <div class="owner-role">OWNER &amp; HANDYMAN</div>
    <ul class="perks">
      <li>Fast Response</li>
      <li>High Quality</li>
      <li>Fair Pricing</li>
      <li>Veteran Owned</li>
    </ul>
  </div>

  <div class="services-title">SERVICES:</div>
  <ul class="services" style="left:18px;top:264px">
    <li>Assembly</li><li>Small Repairs</li><li>Wifi / Router Setup</li><li>Fabrication</li>
  </ul>
  <ul class="services" style="left:155px;top:264px">
    <li>Hanging Items</li><li>Wireless Device Setup</li><li>Odd Jobs</li>
  </ul>

  <div class="contact-bar">
    <span class="contact"><svg width="15" height="15" viewBox="0 0 16 16"><circle cx="8" cy="8" r="8" fill="#fff"/><path d="M8 3.5a3 3 0 0 0-3 3c0 2.2 3 5.5 3 5.5s3-3.3 3-5.5a3 3 0 0 0-3-3z" fill="var(--ink)"/><circle cx="8" cy="6.5" r="1.1" fill="#fff"/></svg>Harbor Point, Florida</span>
    <span class="contact"><svg width="15" height="15" viewBox="0 0 16 16"><circle cx="8" cy="8" r="8" fill="#fff"/><rect x="4" y="5" width="8" height="6" fill="none" stroke="var(--ink)"/><path d="M4 5l4 3.5L12 5" fill="none" stroke="var(--ink)"/></svg>Service@Briskhive360.com</span>
    <span class="contact"><svg width="15" height="15" viewBox="0 0 16 16"><circle cx="8" cy="8" r="8" fill="#fff"/><path d="M5.5 4l1.5 2-1 1c.6 1.3 1.7 2.4 3 3l1-1 2 1.5-1 1.5c-3 0-6.5-3.5-6.5-6.5z" fill="var(--ink)"/></svg>(555) 014-2290 <span class="text-flag">TEXT</span></span>
    <span class="contact"><svg width="15" height="15" viewBox="0 0 16 16"><circle cx="8" cy="8" r="8" fill="#fff"/><g fill="none" stroke="var(--ink)" stroke-width=".9"><circle cx="8" cy="8" r="4"/><ellipse cx="8" cy="8" rx="1.7" ry="4"/><path d="M4 8h8"/></g></svg>Briskhive360.com</span>
  </div>
</section>

<section class="card card--back" aria-label="Postcard back">
  <div class="back-block"></div>
  <div class="brand-title" style="left:27px;top:17px">BRISK HIVE 360</div>
  <div class="brand-rule" style="left:28px;top:55px;width:226px"></div>
  <div class="brand-sub" style="left:27px;top:59px">HANDYMAN</div>

  <div class="mark" style="left:40px;top:111px;font-size:11px"><span class="mark__dot" style="width:12px;height:12px"></span>BRISK HIVE 360</div>
  <div class="badge" role="img" aria-label="Veteran owned business badge" style="left:160px;top:92px;width:60px;height:60px"></div>

  <div class="photo" role="img" aria-label="Collage of handyman work: furniture assembly, hardware parts, smart doorbell install and wifi setup" style="left:50px;top:166px;width:179px;height:121px;border-radius:10px;background:linear-gradient(135deg,#c9a57a,#e8e2d6 45%,#6f7378 60%,#1b6fb0)"></div>
  <svg class="shape" width="285" height="299" viewBox="0 0 285 299" aria-hidden="true">
    <polygon points="40,296 250,287 250,290 40,299" fill="var(--yellow)"/>
  </svg>

  <ul class="back-contacts">
    <li class="contact"><svg width="9" height="9" viewBox="0 0 16 16"><path d="M8 1a5 5 0 0 0-5 5c0 4 5 9 5 9s5-5 5-9a5 5 0 0 0-5-5z" fill="var(--ink)"/></svg>Harbor Point, Florida</li>
    <li class="contact"><svg width="9" height="9" viewBox="0 0 16 16"><rect x="1" y="3" width="14" height="10" fill="none" stroke="var(--ink)" stroke-width="2"/></svg>Service@Briskhive360.com</li>
    <li class="contact"><svg width="9" height="9" viewBox="0 0 16 16"><circle cx="8" cy="8" r="8" fill="var(--ink)"/></svg>(555) 014-2290 <span class="text-flag">TEXT</span></li>
    <li class="contact"><svg width="9" height="9" viewBox="0 0 16 16"><circle cx="8" cy="8" r="7" fill="none" stroke="var(--ink)" stroke-width="2"/></svg>Briskhive360.com</li>
  </ul>

  <div class="stamp-box"></div>
</section>

</body>
</html>
```